Banner Pop Up Opt In Form REDESIGNS - SLEEK BLACK LOOK

Please redesign banners attached.

I am looking for a very sleek look....I do not like this collage of images on these current designs. Please keep all content same but use images that pop.

I have an acccount at www.pixelbarn-demo.com or you can use your own images.

I like black background for somereason because it looks very sleek....but these designs should pop , build trust and credibility and have easy opt in form....SLEEK AND MODERN LOOK is what im looking for....

Target Market(s)

Consumers on websites

Requirements
Must have
• Please redesign banners attached.

Nice to have

Should not have

```html
<!DOCTYPE html>
<html lang="en">
<head>
<meta charset="utf-8">
<title>Opt-In Banner Set – Sleek Black</title>
<link href="https://fonts.googleapis.com/css2?family=Oswald:wght@400;500;600;700&family=Open+Sans:wght@400;800&display=swap" rel="stylesheet">
<style>
  :root{
    --page:#ffffff;
    --black:#000000;
    --white:#ffffff;
    --field-text:#555555;
    --gold-light:#fff3a8;
    --gold:#f2c21a;
    --gold-mid:#c98a0c;
    --gold-dark:#6b3e02;
    --btn-hot:#ffe000;
    --btn-edge:#b87800;
  }
  *{box-sizing:border-box;margin:0;padding:0}
  html,body{width:1200px;height:2500px;overflow:hidden;background:var(--page)}
  .sheet{
    width:1200px;height:2500px;
    display:grid;
    grid-template-columns:518px 518px;
    grid-auto-rows:445px;
    column-gap:33px;row-gap:40px;
    padding:53px 0 0 68px;
  }
  .banner{position:relative;overflow:hidden;background:var(--black);font-family:"Oswald",sans-serif;color:var(--white)}
  .banner__photo{position:absolute;inset:0}
  .banner__shade{position:absolute;inset:0;background:linear-gradient(180deg,var(--black) 0%,rgba(0,0,0,.85) 28%,rgba(0,0,0,0) 55%)}
  .gold{
    background:linear-gradient(180deg,var(--gold-light) 0%,var(--gold) 35%,var(--gold-mid) 60%,var(--gold-dark) 80%,var(--gold) 100%);
    -webkit-background-clip:text;background-clip:text;color:transparent;
  }
  .banner__title{position:absolute;left:0;right:0;text-align:center;font-weight:700;line-height:1;text-transform:uppercase}
  .banner--win .banner__title{top:16px;font-size:78px;letter-spacing:2px}
  .banner--offer .banner__title{top:30px;font-size:50px;letter-spacing:0}
  .banner__lead{position:absolute;left:0;right:0;text-align:center;font-weight:500;font-size:15.5px;text-transform:uppercase;letter-spacing:-.1px}
  .banner--win .banner__lead{top:99px}
  .banner--offer .banner__lead{top:89px}
  .banner__prize{position:absolute;left:0;right:0;text-align:center;font-weight:500;font-size:39px;line-height:39px;text-transform:uppercase}
  .banner--win .banner__prize{top:131px}
  .banner--offer .banner__prize{top:133px}
  .banner--offer .banner__prize.one-line{top:140px}
  .banner--offer .banner__prize.small{font-size:36px}
  .form{position:absolute;left:38px;top:232px;width:252px}
  .form__field{
    display:block;height:32px;margin-bottom:8.5px;border-radius:6px;background:var(--white);
    font-family:"Open Sans",sans-serif;font-size:12.5px;color:var(--field-text);line-height:32px;padding-left:13px;
  }
  .form__submit{
    display:block;margin-top:10px;height:33px;border-radius:6px;
    border:2px solid var(--btn-edge);
    background:radial-gradient(ellipse at 70% 40%,#fff8c0 0%,var(--btn-hot) 30%,#ffb800 70%,#e89a00 100%);
    font-family:"Open Sans",sans-serif;font-weight:800;font-size:14px;color:var(--black);text-align:center;line-height:29px;letter-spacing:.5px;
  }
  .banner__note{position:absolute;left:0;right:0;top:412px;text-align:center;font-size:12.5px;font-weight:500}

  /* photo fills */
  .photo--vegas-strip{background:radial-gradient(ellipse at 75% 65%,#c2661a 0%,#5a2a10 30%,transparent 60%),linear-gradient(180deg,#000 0%,#0b1a22 45%,#12303a 70%,#1a1208 100%)}
  .photo--vegas-night{background:radial-gradient(ellipse at 30% 55%,#8a6a3a 0%,transparent 45%),radial-gradient(ellipse at 85% 85%,#5a2030 0%,transparent 40%),linear-gradient(180deg,#0b0f1c 0%,#1c2430 40%,#3a3026 70%,#1b1410 100%)}
  .photo--fitness-athlete{background:radial-gradient(ellipse at 80% 75%,#4a4244 0%,#1a1618 40%,transparent 65%),linear-gradient(180deg,#000 0%,#0b0b0e 55%,#151535 100%)}
  .photo--fitness-watch{background:radial-gradient(ellipse at 85% 60%,#3b3b3b 0%,#121212 35%,#000 60%)}
  .photo--dessert-table{background:radial-gradient(ellipse at 20% 40%,#b86a86 0%,transparent 40%),radial-gradient(ellipse at 70% 70%,#6a2a2a 0%,transparent 45%),linear-gradient(180deg,#000 0%,#3a2a40 35%,#8a6a88 60%,#c8c4d0 100%)}
  .photo--dining-room{background:radial-gradient(ellipse at 70% 70%,#b88a5a 0%,#5a3a22 35%,transparent 65%),linear-gradient(180deg,#000 0%,#0b0a08 40%,#2a1c12 75%,#4a3422 100%)}
  .photo--hotel-pool{background:radial-gradient(ellipse at 50% 45%,#8a7a66 0%,transparent 45%),linear-gradient(180deg,#000 0%,#1a1814 40%,#2a4a6a 62%,#1e5a8a 80%,#163a62 100%)}
  .photo--resort-dusk{background:radial-gradient(ellipse at 65% 82%,#d4a04a 0%,transparent 30%),linear-gradient(180deg,#000 0%,#08142e 35%,#1c3a7a 60%,#142a50 80%,#0a1426 100%)}
  .photo--resort-night{background:radial-gradient(ellipse at 50% 85%,#2a8aff 0%,#1050c0 25%,transparent 55%),radial-gradient(ellipse at 70% 60%,#6a4a1a 0%,transparent 35%),linear-gradient(180deg,#000 0%,#0a0c10 40%,#141c2a 70%,#0a2a7a 100%)}
  .photo--resort-pool{background:radial-gradient(ellipse at 70% 70%,#2ab4c0 0%,#10707a 30%,transparent 55%),linear-gradient(180deg,#000 0%,#050a10 38%,#0e2a3a 55%,#1a5a5a 75%,#0a1e22 100%)}
</style>
</head>
<body>
<main class="sheet">

  <section class="banner banner--win">
    <div class="banner__photo photo--vegas-strip" role="img" aria-label="Las Vegas strip at night with lit casino hotels"></div>
    <div class="banner__shade"></div>
    <h1 class="banner__title gold">Enter to Win</h1>
    <p class="banner__lead">Subscribe to our newsletter to enter to win a</p>
    <h2 class="banner__prize gold">1-4 Night Las Vegas<br>Hotel &amp; Casino</h2>
    <div class="form"><span class="form__field">Name</span><span class="form__field">e-mail</span><span class="form__field">Phone</span><span class="form__submit">SUBMIT</span></div>
    <p class="banner__note">We will send a e-mail a text message with the offer and instruction on how to redeem.</p>
  </section>

  <section class="banner banner--offer">
    <div class="banner__photo photo--vegas-night" role="img" aria-label="Aerial view of Las Vegas boulevard at night"></div>
    <div class="banner__shade"></div>
    <h1 class="banner__title gold">Want a Great Offer?</h1>
    <p class="banner__lead">Subscribe to our newsletter and received a complimentary</p>
    <h2 class="banner__prize gold">1-4 Night Las Vegas<br>Hotel &amp; Casino</h2>
    <div class="form"><span class="form__field">Name</span><span class="form__field">e-mail</span><span class="form__field">Phone</span><span class="form__submit">SUBMIT</span></div>
    <p class="banner__note">We will send a e-mail a text message with the offer and instruction on how to redeem.</p>
  </section>

  <section class="banner banner--win">
    <div class="banner__photo photo--fitness-athlete" role="img" aria-label="Athlete resting on a mat beside a large fitness watch"></div>
    <div class="banner__shade"></div>
    <h1 class="banner__title gold">Enter to Win</h1>
    <p class="banner__lead">Subscribe to our newsletter to enter to win a</p>
    <h2 class="banner__prize gold" style="font-size:46px;top:136px">Smart Fitness Watch</h2>
    <div class="form"><span class="form__field">Name</span><span class="form__field">e-mail</span><span class="form__field">Phone</span><span class="form__submit">SUBMIT</span></div>
    <p class="banner__note">We will send a e-mail a text message with the offer and instruction on how to redeem.</p>
  </section>

  <section class="banner banner--offer">
    <div class="banner__photo photo--fitness-watch" role="img" aria-label="Close-up of a smart fitness watch on black"></div>
    <h1 class="banner__title gold">Want a Great Offer?</h1>
    <p class="banner__lead">Subscribe to our newsletter and received a complimentary</p>
    <h2 class="banner__prize gold one-line small">Smart Fitness Watch</h2>
    <div class="form"><span class="form__field">Name</span><span class="form__field">e-mail</span><span class="form__field">Phone</span><span class="form__submit">SUBMIT</span></div>
    <p class="banner__note">We will send a e-mail a text message with the offer and instruction on how to redeem.</p>
  </section>

  <section class="banner banner--win">
    <div class="banner__photo photo--dessert-table" role="img" aria-label="Restaurant table with dessert, glasses and flowers"></div>
    <div class="banner__shade"></div>
    <h1 class="banner__title gold">Enter to Win</h1>
    <p class="banner__lead">Subscribe to our newsletter to enter to win a</p>
    <h2 class="banner__prize gold" style="top:145px">$300 Restaurant Certificate</h2>
    <div class="form"><span class="form__field">Name</span><span class="form__field">e-mail</span><span class="form__field">Phone</span><span class="form__submit">SUBMIT</span></div>
    <p class="banner__note">We will send a e-mail a text message with the offer and instruction on how to redeem.</p>
  </section>

  <section class="banner banner--offer">
    <div class="banner__photo photo--dining-room" role="img" aria-label="Elegant dining table set with glasses and flowers"></div>
    <div class="banner__shade"></div>
    <h1 class="banner__title gold">Want a Great Offer?</h1>
    <p class="banner__lead">Subscribe to our newsletter and received a complimentary</p>
    <h2 class="banner__prize gold one-line">$300 Restaurant Certificate</h2>
    <div class="form"><span class="form__field">Name</span><span class="form__field">e-mail</span><span class="form__field">Phone</span><span class="form__submit">SUBMIT</span></div>
    <p class="banner__note">We will send a e-mail a text message with the offer and instruction on how to redeem.</p>
  </section>

  <section class="banner banner--win">
    <div class="banner__photo photo--hotel-pool" role="img" aria-label="Hotel terrace overlooking a blue swimming pool"></div>
    <div class="banner__shade"></div>
    <h1 class="banner__title gold">Enter to Win</h1>
    <p class="banner__lead">Subscribe to our newsletter to enter to win a</p>
    <h2 class="banner__prize gold" style="top:135px">$500 Hotel Savings Cards</h2>
    <div class="form"><span class="form__field">Name</span><span class="form__field">e-mail</span><span class="form__field">Phone</span><span class="form__submit">SUBMIT</span></div>
    <p class="banner__note">We will send a e-mail a text message with the offer and instruction on how to redeem.</p>
  </section>

  <section class="banner banner--offer">
    <div class="banner__photo photo--resort-dusk" role="img" aria-label="Resort pavilion with palm trees at dusk"></div>
    <div class="banner__shade"></div>
    <h1 class="banner__title gold">Want a Great Offer?</h1>
    <p class="banner__lead">Subscribe to our newsletter and received a complimentary</p>
    <h2 class="banner__prize gold one-line small">$500 Hotel Savings Cards</h2>
    <div class="form"><span class="form__field">Name</span><span class="form__field">e-mail</span><span class="form__field">Phone</span><span class="form__submit">SUBMIT</span></div>
    <p class="banner__note">We will send a e-mail a text message with the offer and instruction on how to redeem.</p>
  </section>

  <section class="banner banner--win">
    <div class="banner__photo photo--resort-night" role="img" aria-label="Tropical resort with lit pool and palm trees at night"></div>
    <div class="banner__shade"></div>
    <h1 class="banner__title gold">Enter to Win</h1>
    <p class="banner__lead">Subscribe to our newsletter to enter to win a</p>
    <h2 class="banner__prize gold" style="font-size:34px;line-height:33px;top:133px">7 Night Resort/Condo<br>3500 + Locations</h2>
    <div class="form"><span class="form__field">Name</span><span class="form__field">e-mail</span><span class="form__field">Phone</span><span class="form__submit">SUBMIT</span></div>
    <p class="banner__note">We will send a e-mail a text message with the offer and instruction on how to redeem.</p>
  </section>

  <section class="banner banner--offer">
    <div class="banner__photo photo--resort-pool" role="img" aria-label="Resort infinity pool by the sea with palm trees"></div>
    <div class="banner__shade"></div>
    <h1 class="banner__title gold">Want a Great Offer?</h1>
    <p class="banner__lead">Subscribe to our newsletter and received a complimentary</p>
    <h2 class="banner__prize gold" style="font-size:34px;line-height:33px;top:122px">7 Night Resort/Condo<br>3500 + Locations</h2>
    <div class="form"><span class="form__field">Name</span><span class="form__field">e-mail</span><span class="form__field">Phone</span><span class="form__submit">SUBMIT</span></div>
    <p class="banner__note">We will send a e-mail a text message with the offer and instruction on how to redeem.</p>
  </section>

</main>
</body>
</html>
```